Bramblefox Towing Website

New Pittsburgh, PA towing company looking for a unique and easy to use website with a professional look. We would like the customer to feel confident when booking with us. We offer reliable services with no hidden fees or predatory towing tactics. Designs that incorporate our logo & color scheme are preferred. Looking for websites designed similar to https://steadfallhaulandlift.example/

```html
<!DOCTYPE html>
<html lang="en">
<head>
<meta charset="utf-8">
<title>Bramblefox Towing</title>
<link href="https://fonts.googleapis.com/css2?family=Cormorant+Garamond:wght@400;500;600&family=Poppins:wght@600;700&family=Inter:wght@400;500;600;700&display=swap" rel="stylesheet">
<style>
:root{
  --gold:#d4a52b;
  --ink:#161616;
  --char:#1b1b1b;
  --maroon:#6a1414;
  --icon-red:#7b1a1c;
  --text:#3a3a3a;
  --mist:#eeeded;
  --blush:#f3efef;
  --white:#fff;
}
*{box-sizing:border-box;margin:0;padding:0}
html,body{width:1200px;height:4598px;overflow:hidden;background:var(--white)}
body{font-family:"Inter",sans-serif;color:var(--text);position:relative}
.abs{position:absolute}
section,header,footer{position:absolute;left:0;width:1200px;overflow:hidden}
.btn{position:absolute;display:flex;align-items:center;justify-content:center;background:var(--gold);color:var(--white);font-weight:700;text-transform:uppercase;letter-spacing:.3px}
.para{position:absolute;font-size:14.5px;line-height:22.5px;color:var(--text)}

/* header */
.site-header{top:0;height:141px;background:var(--ink)}
.brand{left:146px;top:34px;display:flex;align-items:center;gap:12px}
.brand-dot{width:22px;height:22px;border-radius:50%;background:var(--gold)}
.brand-name{font-family:"Cormorant Garamond",serif;font-size:34px;font-weight:500;color:var(--gold)}
.appt{left:600px;top:25px;width:193px;height:43px;font-size:15px}
.call{left:832px;top:28px}
.call-label{left:907px;top:22px;color:var(--white);font-family:"Cormorant Garamond",serif;font-size:15px}
.call-num{left:907px;top:40px;color:var(--white);font-size:23px;font-weight:600}
.divider-v{left:885px;top:26px;width:2px;height:40px;background:var(--white)}
.nav{top:96px;font-family:"Cormorant Garamond",serif;font-size:19px;color:var(--white);font-weight:500}
.nav.active{color:var(--gold);text-decoration:underline;text-underline-offset:4px}

/* hero */
.hero{top:141px;height:591px;background:linear-gradient(180deg,#3f5a2a 0%,#557a3a 45%,#8b8d7e 72%,#6f6e68 100%)}
.hero-title{width:1200px;text-align:center;top:68px;font-family:"Poppins",sans-serif;font-weight:700;font-size:58px;color:var(--white);text-shadow:0 3px 8px rgba(0,0,0,.4)}
.hero-sub{width:1200px;text-align:center;top:155px;font-family:"Poppins",sans-serif;font-weight:600;font-size:23px;line-height:33px;color:var(--white);text-shadow:0 2px 6px rgba(0,0,0,.5)}
.hero-btn{left:518px;top:261px;width:162px;height:46px;font-size:16px}
.dots{top:550px;left:562px;display:flex;gap:10px;align-items:center}
.dots span{width:7px;height:7px;border-radius:50%;background:var(--white)}
.dots span.on{width:12px;height:12px;border:2px solid var(--gold);background:var(--white)}

/* welcome */
.welcome{top:732px;height:500px;background:var(--white)}
.welcome-photo{left:132px;top:47px;width:543px;height:396px;background:linear-gradient(180deg,#5a87c0 0%,#a9c3df 35%,#9fa5a3 60%,#55524c 100%)}
.welcome-box{left:598px;top:110px;width:500px;height:350px;background:var(--white)}
.h-section{font-family:"Cormorant Garamond",serif;font-weight:500;color:#222;font-size:28px}
.welcome h2{left:641px;top:146px}
.welcome .rule{left:641px;top:189px;width:282px;height:1px;background:#555}
.welcome .para{left:641px;top:208px;width:395px}
.welcome .btn{left:641px;top:388px;width:100px;height:32px;font-size:11.5px}

/* features */
.features{top:1232px;height:390px;background:linear-gradient(180deg,#ebebea,#f3f3f2)}
.feature{width:260px;text-align:center}
.feature .ico{margin:0 auto;height:80px;display:flex;align-items:flex-end;justify-content:center}
.feature h3{margin-top:40px;font-size:15px;font-weight:700;color:#1d1d1d;line-height:22px}
.feature p{margin-top:10px;font-size:13.5px;line-height:20px;color:#444}

/* towing services */
.services{top:1622px;height:609px;background:var(--char)}
.services h2{left:132px;top:52px;color:var(--white);font-size:29px;letter-spacing:.5px;text-transform:uppercase}
.services .para{left:132px;top:102px;width:390px;color:#d8d8d8;font-size:13.5px;line-height:20px}
.svc-list{left:132px;top:213px;list-style:none}
.svc-list li{height:25.5px;display:flex;align-items:center;gap:14px;color:#d8d8d8;font-size:13.5px}
.services .btn{left:132px;top:525px;width:100px;height:32px;font-size:11.5px}
.services-photo{left:579px;top:0;width:621px;height:609px;background:linear-gradient(160deg,#2f4d22 0%,#5d7a3e 40%,#9c2537 55%,#d7d7d4 75%,#7c7a74 100%)}
.gold-bar{left:571px;width:8px;background:var(--gold)}

/* testimonials */
.testimonials{top:2231px;height:627px;background:var(--white)}
.t-title{width:1200px;text-align:center;top:46px}
.t-rule{left:555px;top:104px;width:90px;height:1px;background:#333}
.card{top:157px;width:302px;height:400px;border:1.5px solid #888;background:var(--white);padding:26px 30px}
.card .quote{font-family:"Cormorant Garamond",serif;font-size:34px;color:var(--gold);line-height:20px;height:22px}
.card .stars{color:var(--gold);font-size:17px;letter-spacing:1px;margin-top:4px}
.card p{margin-top:14px;font-size:13.5px;line-height:20px;color:#444}
.card .who{position:absolute;left:30px;bottom:26px;display:flex;align-items:center;gap:12px;font-size:11.5px;font-weight:700;color:#222;text-transform:uppercase}
.avatar{width:38px;height:38px;border-radius:50%;background:linear-gradient(180deg,#cfd3d8,#8c929a)}
.t-arrow{top:340px}

/* why choose */
.why{top:2858px;height:541px;background:var(--blush)}
.why-title{width:1200px;text-align:center;top:44px}
.why-rule{left:555px;top:98px;width:90px;height:1px;background:#333}
.why-item{display:flex;align-items:center;gap:16px}
.why-icon{width:72px;height:72px;border-radius:50%;background:var(--icon-red);display:flex;align-items:center;justify-content:center}
.why-label{font-family:"Cormorant Garamond",serif;font-weight:600;font-size:21px;line-height:30px;color:#1f1f1f}
.mascot-art{left:312px;top:309px;width:578px;height:232px;background:linear-gradient(180deg,rgba(243,239,239,0) 0%,#d9d3d3 40%,#cbc4c4 100%)}

/* rated */
.rated{top:3399px;height:550px;background:var(--white)}
.rated-photo{left:0;top:0;width:622px;height:550px;background:linear-gradient(150deg,#345a2a 0%,#8a9199 35%,#c9ccd0 55%,#2f3f8e 75%,#bfc4c8 100%)}
.rated h2{left:684px;top:106px;font-size:30px;line-height:38px}
.rated .rule{left:684px;top:190px;width:155px;height:1px;background:#555}
.rated .para{left:684px;top:230px;width:395px}
.rated .btn{left:684px;top:425px;width:100px;height:32px;font-size:11.5px}

/* cta */
.cta{top:3949px;height:295px;background:linear-gradient(180deg,#701616,#5a1010)}
.cta-text{width:1200px;text-align:center;top:56px;font-family:"Cormorant Garamond",serif;font-size:32px;line-height:44px;color:var(--white)}
.cta .btn{left:525px;top:177px;width:150px;height:49px;font-size:15px}

/* footer */
.site-footer{top:4244px;height:354px;background:var(--ink);color:var(--white)}
.f-brand{left:132px;top:120px;display:flex;align-items:center;gap:14px}
.f-brand .brand-dot{width:28px;height:28px}
.f-brand .brand-name{font-size:42px}
.f-head{top:54px;font-size:13px;font-weight:700;letter-spacing:.3px}
.f-links{left:525px;top:90px;list-style:none}
.f-links li{height:20px;font-size:11.5px;text-transform:uppercase}
.f-row{display:flex;gap:12px;align-items:flex-start}
.f-ico{width:22px;height:22px;border-radius:50%;background:var(--white);display:flex;align-items:center;justify-content:center;flex:none;margin-top:2px}
.f-row div{font-size:11.5px;line-height:16px}
.f-line{left:132px;top:271px;width:936px;height:1px;background:#3a3a3a}
.copy{width:1200px;text-align:center;top:312px;font-size:10px;color:#bbb}
</style>
</head>
<body>

<header class="site-header">
  <div class="abs brand"><span class="brand-dot"></span><span class="brand-name">Bramblefox</span></div>
  <div class="btn appt">Get Appointment</div>
  <svg class="abs call" width="40" height="40" viewBox="0 0 40 40" fill="none" stroke="#fff" stroke-width="2"><path d="M10 6l6 7-4 4c2 5 6 9 11 11l4-4 7 6-4 5C18 34 6 22 5 10z"/><path d="M24 8a9 9 0 0 1 8 8M24 2a15 15 0 0 1 14 14"/></svg>
  <div class="abs divider-v"></div>
  <div class="abs call-label">Call Us</div>
  <div class="abs call-num">412.555.0148</div>
  <div class="abs nav active" style="left:461px">Home</div>
  <div class="abs nav" style="left:550px">About Us</div>
  <div class="abs nav" style="left:673px">Services</div>
  <div class="abs nav" style="left:784px">Areas</div>
  <div class="abs nav" style="left:875px">Reviews</div>
  <div class="abs nav" style="left:977px">Contact Us</div>
</header>

<section class="hero" role="img" aria-label="Photo of a white flatbed tow truck loading a red hatchback in front of green trees">
  <h1 class="abs hero-title">PA TOWING</h1>
  <p class="abs hero-sub">Lorem Ipsum is simply dummy text of<br>the printing and typesetting</p>
  <div class="btn hero-btn">Call Us Now</div>
  <div class="abs dots"><span></span><span></span><span class="on"></span><span></span><span></span></div>
</section>

<section class="welcome">
  <div class="abs welcome-photo" role="img" aria-label="Photo of a white car on a flatbed tow truck under a blue sky"></div>
  <div class="abs welcome-box"></div>
  <h2 class="abs h-section">Welcome to Bramblefox</h2>
  <div class="abs rule"></div>
  <p class="para">There are many variations of passages of Lorem Ipsum available, but the majority have suffered alteration in some form, by injected humour, or randomised words which don't look even slightly believable. If you are going to use a passage of Lorem Ipsum, you need to be sure there isn't anything embarrassing hidden in the middle of text.</p>
  <div class="btn">Read More</div>
</section>

<section class="features">
  <div class="abs feature" style="left:129px;top:54px">
    <div class="ico"><svg width="120" height="76" viewBox="0 0 120 76" fill="var(--icon-red)"><circle cx="34" cy="16" r="13"/><path d="M10 76V46c0-10 10-16 24-16s24 6 24 16v30z"/><circle cx="84" cy="14" r="12"/><path d="M62 76V44c0-9 10-15 22-15s22 6 22 15v32z"/><circle cx="60" cy="38" r="9"/><path d="M46 76V60c0-6 6-10 14-10s14 4 14 10v16z"/></svg></div>
    <h3>FAMILY OWNED &amp; OPERATED</h3>
    <p>Lorem ipsum dolor sit amet, cons ectetur adipiscing elit, sed do eiusmod tempor incididunt ut labore et dolore magna aliqua. Ut enim ad minim veni am, quis nostrud exercitation ulla mco laboris nisi ut aliquip.</p>
  </div>
  <div class="abs feature" style="left:470px;top:54px">
    <div class="ico"><svg width="120" height="60" viewBox="0 0 120 60" fill="var(--icon-red)"><path d="M40 14h34l10 14h22v18H40z"/><path d="M4 38L30 14l4 4-24 22z"/><circle cx="56" cy="48" r="9" stroke="#eee" stroke-width="3"/><circle cx="94" cy="48" r="9" stroke="#eee" stroke-width="3"/><circle cx="6" cy="46" r="5" fill="none" stroke="var(--icon-red)" stroke-width="3"/></svg></div>
    <h3>ROADSIDE ASSISTANCE</h3>
    <p>Lorem ipsum dolor sit amet, cons ectetur adipiscing elit, sed do eiusmod tempor incididunt ut labore et dolore magna aliqua. Ut enim ad minim veni am, quis nostrud exercitation ulla mco laboris nisi ut aliquip.</p>
  </div>
  <div class="abs feature" style="left:817px;top:54px">
    <div class="ico"><svg width="70" height="70" viewBox="0 0 70 70"><circle cx="40" cy="30" r="22" fill="none" stroke="var(--icon-red)" stroke-width="5"/><text x="40" y="38" text-anchor="middle" font-family="Inter,sans-serif" font-weight="700" font-size="21" fill="var(--icon-red)">24</text><path d="M6 30l8-6 8 10-5 5c3 7 8 12 15 15l5-5 10 8-6 8C22 64 4 46 6 30z" fill="var(--icon-red)"/></svg></div>
    <h3>24 HOUR EMERGENCY<br>SERVICE AVAILABLE</h3>
    <p>Lorem ipsum dolor sit amet, cons ectetur adipiscing elit, sed do eiusmod tempor incididunt ut labore et dolore magna aliqua. Ut enim ad minim veni am, quis nostrud exercitation ulla mco laboris nisi ut aliquip.</p>
  </div>
</section>

<section class="services">
  <h2 class="abs h-section">Towing Services</h2>
  <p class="para">Lorem ipsum dolor sit amet, cons ectetur adipiscing elit, sed do eiusmod tempor incididunt ut labore et dolore magna aliqua. Ut enim ad minim veni am, quis nostrud exercitation ulla mco laboris nisi ut aliquip.</p>
  <ul class="abs svc-list">
    <li><svg width="12" height="10" viewBox="0 0 12 10"><path d="M1 5l3.5 3.5L11 1.5" fill="none" stroke="#fff" stroke-width="2.2"/></svg>Light-Duty Towing</li>
    <li><svg width="12" height="10" viewBox="0 0 12 10"><path d="M1 5l3.5 3.5L11 1.5" fill="none" stroke="#fff" stroke-width="2.2"/></svg>Accident Recovery</li>
    <li><svg width="12" height="10" viewBox="0 0 12 10"><path d="M1 5l3.5 3.5L11 1.5" fill="none" stroke="#fff" stroke-width="2.2"/></svg>Roadside Assistance</li>
    <li><svg width="12" height="10" viewBox="0 0 12 10"><path d="M1 5l3.5 3.5L11 1.5" fill="none" stroke="#fff" stroke-width="2.2"/></svg>Lockout Service</li>
    <li><svg width="12" height="10" viewBox="0 0 12 10"><path d="M1 5l3.5 3.5L11 1.5" fill="none" stroke="#fff" stroke-width="2.2"/></svg>Battery Service</li>
    <li><svg width="12" height="10" viewBox="0 0 12 10"><path d="M1 5l3.5 3.5L11 1.5" fill="none" stroke="#fff" stroke-width="2.2"/></svg>Tire Service</li>
    <li><svg width="12" height="10" viewBox="0 0 12 10"><path d="M1 5l3.5 3.5L11 1.5" fill="none" stroke="#fff" stroke-width="2.2"/></svg>Long-Distance Towing</li>
    <li><svg width="12" height="10" viewBox="0 0 12 10"><path d="M1 5l3.5 3.5L11 1.5" fill="none" stroke="#fff" stroke-width="2.2"/></svg>Winching</li>
    <li><svg width="12" height="10" viewBox="0 0 12 10"><path d="M1 5l3.5 3.5L11 1.5" fill="none" stroke="#fff" stroke-width="2.2"/></svg>Motorcycle Towing</li>
    <li><svg width="12" height="10" viewBox="0 0 12 10"><path d="M1 5l3.5 3.5L11 1.5" fill="none" stroke="#fff" stroke-width="2.2"/></svg>Medium-Duty Towing</li>
    <li><svg width="12" height="10" viewBox="0 0 12 10"><path d="M1 5l3.5 3.5L11 1.5" fill="none" stroke="#fff" stroke-width="2.2"/></svg>Toolbox Relocation</li>
  </ul>
  <div class="btn">Read More</div>
  <div class="abs services-photo" role="img" aria-label="Photo of a red hatchback on the yellow bed of a white tow truck"></div>
  <div class="abs gold-bar" style="top:0;height:134px"></div>
  <div class="abs gold-bar" style="top:423px;height:134px"></div>
</section>

<section class="testimonials">
  <h2 class="abs h-section t-title">Customer Testimonials</h2>
  <div class="abs t-rule"></div>
  <svg class="abs t-arrow" style="left:58px" width="28" height="20" viewBox="0 0 28 20" fill="none" stroke="#777" stroke-width="2"><path d="M27 10H2M10 2L2 10l8 8"/></svg>
  <svg class="abs t-arrow" style="left:1108px" width="28" height="20" viewBox="0 0 28 20" fill="none" stroke="#777" stroke-width="2"><path d="M1 10h25M18 2l8 8-8 8"/></svg>
  <div class="abs card" style="left:132px"><div class="quote">&ldquo;</div><div class="stars">★★★★★</div><p>Sed ut perspiciatis unde omnis iste natus error sit voluptatem accusa ntium doloremque laudantium, totam rem aperiam, eaque ipsa quae ab illo inventore veritatis et quasi architecto beatae vitae dicta sunt explicabo. Nemo enim ipsam voluptatem quia voluptas sit aspernatur aut odit aut fugit, sed quia consequuntur magni dolores eos qui ratione voluptatem sequi nesciunt.</p><div class="who"><span class="avatar"></span>Dalton</div></div>
  <div class="abs card" style="left:449px"><div class="quote">&ldquo;</div><div class="stars">★★★★★</div><p>Sed ut perspiciatis unde omnis iste natus error sit voluptatem accusa ntium doloremque laudantium, totam rem aperiam, eaque ipsa quae ab illo inventore veritatis et quasi architecto beatae vitae dicta sunt explicabo. Nemo enim ipsam voluptatem quia voluptas sit aspernatur aut odit aut fugit, sed quia consequuntur magni dolores eos qui ratione voluptatem sequi nesciunt.</p><div class="who"><span class="avatar"></span>Dalton</div></div>
  <div class="abs card" style="left:768px"><div class="quote">&ldquo;</div><div class="stars">★★★★★</div><p>Sed ut perspiciatis unde omnis iste natus error sit voluptatem accusa ntium doloremque laudantium, totam rem aperiam, eaque ipsa quae ab illo inventore veritatis et quasi architecto beatae vitae dicta sunt explicabo. Nemo enim ipsam voluptatem quia voluptas sit aspernatur aut odit aut fugit, sed quia consequuntur magni dolores eos qui ratione voluptatem sequi nesciunt.</p><div class="who"><span class="avatar"></span>Dalton</div></div>
</section>

<section class="why">
  <h2 class="abs h-section why-title">Why Choose us</h2>
  <div class="abs why-rule"></div>
  <div class="abs why-item" style="left:341px;top:148px">
    <div class="why-icon"><svg width="38" height="34" viewBox="0 0 38 34" fill="none" stroke="#fff" stroke-width="2.5"><path d="M2 12L19 2l17 10v20H2z"/><path d="M9 32V16h20v16M9 21h20M9 26h20"/></svg></div>
    <div class="why-label">Secure Storage<br>Facility</div>
  </div>
  <div class="abs why-item" style="left:643px;top:171px">
    <div class="why-icon"><svg width="34" height="34" viewBox="0 0 34 34" fill="#fff"><path d="M3 14h7v18H3zM12 31V15l7-12c3 0 4 2 3 5l-2 5h9c2 0 4 2 3 4l-3 11c-1 2-2 3-4 3z"/></svg></div>
    <div class="why-label">Great Customer<br>Service</div>
  </div>
  <div class="abs why-item" style="left:134px;top:278px">
    <div class="why-icon"><svg width="36" height="36" viewBox="0 0 36 36" fill="none" stroke="#fff" stroke-width="2.5"><path d="M6 20v-4a12 12 0 0 1 24 0v4"/><rect x="3" y="18" width="6" height="9" rx="2" fill="#fff"/><rect x="27" y="18" width="6" height="9" rx="2" fill="#fff"/><path d="M30 27c0 4-4 6-9 6"/></svg></div>
    <div class="why-label">Speak to a Live<br>Agent 24/7</div>
  </div>
  <div class="abs why-item" style="left:898px;top:264px">
    <div class="why-icon"><svg width="44" height="26" viewBox="0 0 44 26" fill="#fff"><path d="M16 4h16l6 8h5v8H16z"/><path d="M2 18L14 6l3 3L6 20z"/><circle cx="23" cy="21" r="4"/><circle cx="37" cy="21" r="4"/></svg></div>
    <div class="why-label">Towing and<br>Recovery</div>
  </div>
  <div class="abs mascot-art" role="img" aria-label="Decorative black brand mascot illustration"></div>
</section>

<section class="rated">
  <div class="abs rated-photo" role="img" aria-label="Photo of a tow operator in blue overalls securing a silver car on a flatbed"></div>
  <h2 class="abs h-section">#1 Rated Towing Company<br>in Pittsburgh</h2>
  <div class="abs rule"></div>
  <p class="para">There are many variations of passages of Lorem Ipsum available, but the majority have suffered alteration in some form, by injected humour, or randomised words which don't look even slightly believable. If you are going to use a passage of Lorem Ipsum, you need to be sure there isn't anything embarrassing hidden in the middle of text.</p>
  <div class="btn">Read More</div>
</section>

<section class="cta">
  <p class="abs cta-text">Lorem ipsum dolor sit amet consectetur adipiscing<br>elit sed do eiusmod tempor incididunt</p>
  <div class="btn">Contact Us</div>
</section>

<footer class="site-footer">
  <div class="abs f-brand"><span class="brand-dot"></span><span class="brand-name">Bramblefox</span></div>
  <div class="abs f-head" style="left:525px">MENU</div>
  <ul class="abs f-links">
    <li>Home</li><li>About Us</li><li>Services</li><li>Areas</li><li>Reviews</li><li>Contact Us</li>
  </ul>
  <div class="abs f-head" style="left:695px">CONTACT US</div>
  <div class="abs f-row" style="left:695px;top:96px"><span class="f-ico"><svg width="10" height="12" viewBox="0 0 10 12"><path d="M5 12S1 7 1 4.5a4 4 0 0 1 8 0C9 7 5 12 5 12z" fill="#161616"/></svg></span><div>2750 Larkmoor Street<br>Pittsburgh, PA 15222</div></div>
  <div class="abs f-row" style="left:695px;top:146px"><span class="f-ico"><svg width="11" height="11" viewBox="0 0 11 11"><path d="M2 1l2 2-1 1.5c1 2 2 3 4 4L8.5 7l2 2L9 10.5C5 10 1 6 .5 2z" fill="#161616"/></svg></span><div>Call Us<br>412.555.0148</div></div>
  <div class="abs f-row" style="left:695px;top:196px"><span class="f-ico"><svg width="12" height="9" viewBox="0 0 12 9"><rect x="0" y="0" width="12" height="9" rx="1" fill="#161616"/><path d="M1 1l5 4 5-4" stroke="#fff" fill="none"/></svg></span><div>E-mail Us<br>info@bramblefox.example</div></div>
  <div class="abs f-head" style="left:963px">FOLLOW US</div>
  <div class="abs f-row" style="left:963px;top:96px"><span class="f-ico"></span><div>Like us on<br>PAGEFEED</div></div>
  <div class="abs f-row" style="left:963px;top:146px"><span class="f-ico"></span><div>Follow us on<br>CHIRPLINE</div></div>
  <div class="abs f-row" style="left:963px;top:196px"><span class="f-ico"></span><div>Follow us on<br>WORKLINK</div></div>
  <div class="abs f-line"></div>
  <div class="abs copy">Copyright © 2021 All Rights Reserved</div>
</footer>

</body>
</html>
```